Software Company Requires Website

We need a web design for a new mobile software development company based in London named Velquin Solutions.
The design needs to be clean and smooth. Not too flashy, not too boring.
I would like to try the design with some warm colors, and maybe a headline or something highlighted with a strong color. ( logo ? ) The layout should be something like the bellow links, all in one page.

http://brantelo.net/
http://www.kelvory.com/
http://www.work-plover.de/
http://www.tusker.com/
http://www.quildenta.com/us/

Now some of them they seem different from the others, but in each of them there is something that ticks my brain, so it`s up to you to surprise me.

I have uploaded the logo of the company, so you guys can fit that in your design as well.
Updates

Hy everybody This will be the last update for the brief. The company will focus in the beginning for mobile development only, so i would like the website design to be done in a matter that will reflect that. We will develop ORBIS, Nimble and Panea applications. We will also require 3 pages: One for the home menu, one for portfolio and one for contact us. The layout should be the same ( one page scroll down ) but the design of the 3 pages different. Please readdress the brief. Hope that i provided enough information for the scope of the project.

I have uploaded the logo that you guys can use. If the logo requires small modifications you can adjust that to suit your idea as long as the logo does not change completely.

Target Market(s)

High End companies that require simplified software solutions.

Industry/Entity Type

It Company

Number of Pages Required

3 page

Requirements
Must have
• One page scroll down layout for 3 pages:
• one for home page, one for portfolio and one for contact us.
• In the portfolio page we would like to have different display options for given examples of applications ( min 3 )

```html
<!DOCTYPE html>
<html lang="en">
<head>
<meta charset="utf-8">
<title>Velquin Solutions — Mobile App Development</title>
<link rel="stylesheet" href="https://fonts.googleapis.com/css2?family=Oswald:wght@300;400;500&family=Open+Sans:wght@400;600;700&display=swap">
<style>
:root{
  --blue:#1a8fd6;
  --blue-dark:#0f5f93;
  --blue-nav:#1769a6;
  --hero-a:#1787d0;
  --hero-b:#2ba6e8;
  --ink:#555b61;
  --muted:#8a8f94;
  --rule:#e3e5e7;
  --slate:#4a5058;
  --slate-text:#aab1b9;
  --footer:#3a3e43;
  --footer-box:#4a4f56;
  --footer-bar:#2a2d31;
  --white:#ffffff;
  --pale:#e1e3e5;
}
*{box-sizing:border-box;margin:0;padding:0}
html,body{width:1200px;height:2597px;overflow:hidden}
body{font-family:"Open Sans",Arial,sans-serif;color:var(--ink);background:var(--white);position:relative}
a{color:inherit;text-decoration:none}

/* header */
.site-header{position:absolute;top:0;left:0;width:1200px;height:71px;background:var(--white)}
.brand{position:absolute;left:187px;top:16px;display:flex;align-items:center;gap:10px}
.brand-mark{width:30px;height:30px;border-radius:50%;background:var(--blue)}
.brand-name{font-family:"Oswald",sans-serif;font-weight:400;font-size:22px;color:var(--blue);letter-spacing:.5px}
.main-nav{position:absolute;left:708px;top:21px;display:flex;gap:4px}
.main-nav a{font-family:"Oswald",sans-serif;font-size:13px;color:#777;padding:6px 6px;line-height:16px}
.main-nav a.active{background:#e7f2fa;color:var(--blue)}
.phone-cta{position:absolute;left:909px;top:19px;width:145px;height:31px;background:var(--blue-nav);color:var(--white);
  font-family:"Oswald",sans-serif;font-size:16px;display:flex;align-items:center;justify-content:center;gap:10px}

/* hero */
.hero{position:absolute;top:71px;left:0;width:1200px;height:436px;
  background:radial-gradient(ellipse 700px 380px at 700px 120px,#3fb3ee 0%,rgba(63,179,238,0) 70%),linear-gradient(180deg,var(--hero-b),var(--hero-a))}
.hero-device{position:absolute;left:216px;top:36px;width:220px;height:400px;border-radius:36px 36px 0 0;
  background:linear-gradient(180deg,#f4f5f6,#dfe2e5)}
.hero-arrow{position:absolute;top:180px}
.hero-arrow.left{left:140px}
.hero-arrow.right{left:1063px}
.hero-copy{position:absolute;left:490px;top:64px;width:510px;color:var(--white)}
.hero-copy h1{font-family:"Oswald",sans-serif;font-weight:400;font-size:44px;line-height:50px}
.hero-copy h2{font-family:"Oswald",sans-serif;font-weight:400;font-size:30px;line-height:36px;margin-top:4px}
.hero-copy p{font-size:13px;line-height:19px;margin-top:14px}
.platform-tiles{display:flex;gap:15px;margin-top:24px}
.platform-tile{width:57px;height:54px;background:var(--white);border-radius:3px;box-shadow:0 6px 10px rgba(0,0,0,.12);
  display:flex;align-items:center;justify-content:center}
.platform-tile span{width:22px;height:22px;border-radius:4px;background:var(--blue)}
.btn-quote{display:inline-block;margin-top:24px;width:204px;height:42px;line-height:42px;text-align:center;background:var(--blue-dark);
  font-family:"Oswald",sans-serif;font-size:15px;letter-spacing:1px;color:var(--white)}
.slider-dots{position:absolute;display:flex;gap:4px}
.slider-dots i{width:10px;height:10px;border-radius:50%;border:1px solid rgba(0,0,0,.35);background:rgba(255,255,255,.35)}
.slider-dots i.on{background:rgba(0,0,0,.35)}

/* welcome */
.welcome{position:absolute;top:507px;left:0;width:1200px;height:298px}
.section-title{font-family:"Oswald",sans-serif;font-weight:300;font-size:30px;color:#666;text-align:center}
.section-title strong{font-weight:400;color:var(--blue)}
.lead{width:868px;margin:0 auto;font-size:11.5px;line-height:17px;color:var(--muted)}
.welcome .section-title{margin-top:26px}
.welcome .lead{margin-top:12px}
.feature-row{position:absolute;top:156px;left:0;width:1200px}
.feature{position:absolute;width:160px;text-align:center}
.feature-icon{width:97px;height:97px;border-radius:50%;background:var(--pale);margin:0 auto;display:flex;align-items:center;justify-content:center}
.feature.active .feature-icon{background:var(--blue)}
.feature-label{font-family:"Oswald",sans-serif;font-size:15px;color:#555;margin-top:10px}
.pointer{position:absolute;left:256px;top:291px;width:0;height:0;border-left:7px solid transparent;border-right:7px solid transparent;border-bottom:7px solid var(--slate)}

/* technology */
.technology{position:absolute;top:805px;left:0;width:1200px;height:360px;background:var(--slate);color:var(--white)}
.technology h3{font-family:"Oswald",sans-serif;font-weight:300;font-size:30px;text-align:center;margin-top:28px}
.technology .intro{width:700px;margin:10px auto 0;text-align:center;font-size:13px;line-height:20px;color:var(--slate-text)}
.tech-list{position:absolute;top:142px;left:0;width:1200px;list-style:none}
.tech-list li{position:absolute;font-size:12px;display:flex;align-items:center;gap:14px;color:#e9ecef}
.btn-apps{position:absolute;left:497px;top:281px;width:215px;height:41px;line-height:41px;text-align:center;background:var(--blue);
  font-family:"Oswald",sans-serif;font-size:15px;letter-spacing:1px}

/* platforms */
.platforms{position:absolute;top:1165px;left:0;width:1200px;height:480px}
.platforms .section-title{margin-top:18px}
.platforms .lead{margin-top:12px}
.platform-card{position:absolute;top:135px;width:274px;height:328px;border:1px solid var(--rule);text-align:center}
.card-icon{width:97px;height:97px;border:2px solid #5b6066;border-radius:50%;margin:20px auto 0;display:flex;align-items:center;justify-content:center}
.card-icon span{width:30px;height:30px;border-radius:6px;background:#5b6066}
.platform-card h4{font-family:"Oswald",sans-serif;font-weight:400;font-size:25px;letter-spacing:1px;color:#555;margin-top:18px;line-height:30px}
.platform-card .sub{font-family:"Oswald",sans-serif;font-weight:300;font-size:17px;color:var(--blue);line-height:20px}
.platform-card p{font-size:11.5px;line-height:17px;color:var(--muted);width:220px;margin:10px auto 0}
.btn-outline{display:inline-block;margin-top:18px;width:104px;height:34px;line-height:32px;border:1px solid #cfd2d5;
  font-family:"Oswald",sans-serif;font-size:13px;color:#555}

/* showcase */
.showcase{position:absolute;top:1666px;left:0;width:1200px;height:360px}
.showcase-banner{position:absolute;left:187px;top:76px;width:868px;height:191px;
  background:linear-gradient(90deg,#5a3f2a 0%,#8d6a4c 35%,#6b4e36 65%,#3e2c20 100%)}
.showcase-devices{position:absolute;left:211px;top:0;width:374px;height:348px;border-radius:22px;
  background:linear-gradient(180deg,#2c2c2e,#131314)}
.showcase-copy{position:absolute;left:609px;top:96px;color:var(--white)}
.showcase-copy h5{font-family:"Oswald",sans-serif;font-weight:400;font-size:22px;letter-spacing:.5px}
.showcase-actions{display:flex;gap:6px;margin-top:8px}
.square-btn{width:35px;height:35px;border:1px solid rgba(255,255,255,.8);display:flex;align-items:center;justify-content:center}
.square-btn span{width:14px;height:14px;border-radius:3px;background:var(--white)}
.details-btn{height:35px;padding:0 14px;line-height:33px;border:1px solid rgba(255,255,255,.8);font-family:"Oswald",sans-serif;font-size:13px}

/* clients */
.clients{position:absolute;top:2073px;left:187px;width:868px;height:102px;border-top:1px solid var(--rule)}
.client{position:absolute;top:30px;height:36px;background:#c7cacd;border-radius:4px}

/* footer */
.site-footer{position:absolute;top:2175px;left:0;width:1200px;height:370px;background:var(--footer);color:#cfd3d7}
.footer-heading{font-family:"Oswald",sans-serif;font-weight:400;font-size:16px;color:var(--white)}
.blog{position:absolute;left:187px;top:44px;width:300px}
.blog-item{font-size:11.5px;line-height:17px;color:#d4d8dc}
.blog-item time{display:block;font-size:10px;font-weight:700;color:var(--white)}
.newsletter{position:absolute;left:540px;top:44px;width:240px}
.signup{display:flex;margin-top:18px}
.signup .field{width:149px;height:28px;background:#2a2d31;font-size:11px;color:#bbb;padding:6px 8px}
.signup .submit{width:73px;height:28px;background:var(--blue);color:var(--white);font-family:"Oswald",sans-serif;font-size:13px;text-align:center;line-height:28px}
.connect{list-style:none;margin-top:16px}
.connect li{display:flex;align-items:center;gap:12px;font-size:11.5px;height:30px}
.connect li i{width:9px;height:9px;border-radius:50%;background:#aeb3b8}
.contact-box{position:absolute;left:831px;top:36px;width:224px;height:270px;background:var(--footer-box);border-bottom:4px solid var(--blue);padding:26px 30px;font-style:normal}
.contact-box p{font-size:11.5px;line-height:17px;color:#d4d8dc}
.contact-box strong{color:var(--white);font-weight:600}
.footer-bar{position:absolute;top:2545px;left:0;width:1200px;height:52px;background:var(--footer-bar);font-size:10px;color:#8b9096}
.footer-bar .legal{position:absolute;left:187px;top:9px;line-height:17px}
.footer-bar .brand-small{position:absolute;left:952px;top:14px;display:flex;align-items:center;gap:7px}
.footer-bar .brand-small span.dot{width:20px;height:20px;border-radius:50%;background:var(--blue)}
.footer-bar .brand-small span.name{font-family:"Oswald",sans-serif;font-size:15px;color:var(--blue)}
</style>
</head>
<body>

<header class="site-header">
  <a class="brand" href="#"><span class="brand-mark"></span><span class="brand-name">Velquin Solutions</span></a>
  <nav class="main-nav">
    <a class="active" href="#">HOME</a><a href="#">PORTFOLIO</a><a href="#">CONTACT</a>
  </nav>
  <a class="phone-cta" href="#">
    <svg width="13" height="13" viewBox="0 0 24 24" fill="#fff"><path d="M6.6 10.8a15.1 15.1 0 006.6 6.6l2.2-2.2a1 1 0 011-.25 11.4 11.4 0 003.6.57 1 1 0 011 1V20a1 1 0 01-1 1A17 17 0 013 4a1 1 0 011-1h3.5a1 1 0 011 1c0 1.25.2 2.45.57 3.57a1 1 0 01-.25 1z"/></svg>
    +1(555)0142386
  </a>
</header>

<section class="hero">
  <div class="hero-device" role="img" aria-label="Smartphone showing a messaging inbox app"></div>
  <svg class="hero-arrow left" width="34" height="70" viewBox="0 0 34 70"><path d="M32 2L3 35l29 33" fill="none" stroke="#0e5f95" stroke-width="3"/></svg>
  <svg class="hero-arrow right" width="34" height="70" viewBox="0 0 34 70"><path d="M2 2l29 33L2 68" fill="none" stroke="#0e5f95" stroke-width="3"/></svg>
  <div class="hero-copy">
    <h1>WE DEVELOP</h1>
    <h2>ORBIS, NIMBLE AND PANEA APPLICATIONS!</h2>
    <p>Lorem ipsum dolor sit amet, consectetur adipiscing elit. Duis fermentum hendrerit lectus, ut malesuada lectus pharetra quis. Proin iaculis lectus dolor, sit amet gravida quam commodo non.</p>
    <div class="platform-tiles">
      <div class="platform-tile"><span></span></div>
      <div class="platform-tile"><span></span></div>
      <div class="platform-tile"><span></span></div>
    </div>
    <a class="btn-quote" href="#">REQUEST A QUOTE</a>
  </div>
  <div class="slider-dots" style="left:1013px;top:408px"><i></i><i class="on"></i><i></i></div>
</section>

<section class="welcome">
  <h2 class="section-title">Welcome to <strong>Velquin Solutions</strong></h2>
  <p class="lead">Sed semper est risus, a faucibus nibh vestibulum rhoncus. Ut ultrices ullamcorper dapibus. Aenean consequat in nisi eu vehicula. Vivamus et justo a arcu porttitor gravida eget id augue. Curabitur eu volutpat dui. In porta efficitur nunc, quis suscipit tellus congue nec. Nulla vestibulum lacinia sodales. Aenean ornare nisi non nulla faucibus, ac iaculis quam imperdiet. In condimentum nunc tempus, molestie felis vitae, feugiat augue.</p>
  <div class="feature-row">
    <div class="feature active" style="left:183px">
      <div class="feature-icon">
        <svg width="50" height="50" viewBox="0 0 50 50" fill="none" stroke="#fff" stroke-width="3"><circle cx="20" cy="28" r="9"/><circle cx="20" cy="28" r="3"/><path d="M20 15v-4M20 45v-4M7 28H3M37 28h-4M11 19l-3-3M32 40l-3-3M11 37l-3 3M32 16l-3 3"/><circle cx="38" cy="12" r="5"/></svg>
      </div>
      <div class="feature-label">TECHNOLOGY</div>
    </div>
    <div class="feature" style="left:372px">
      <div class="feature-icon"><svg width="46" height="50" viewBox="0 0 46 50" fill="#fff"><path d="M23 4a15 15 0 00-9 27v6h18v-6A15 15 0 0023 4z"/><rect x="15" y="40" width="16" height="4" rx="2"/></svg></div>
      <div class="feature-label">SOLUTIONS</div>
    </div>
    <div class="feature" style="left:557px">
      <div class="feature-icon"><svg width="56" height="44" viewBox="0 0 56 44" fill="#fff"><circle cx="28" cy="12" r="9"/><path d="M12 42c0-10 7-16 16-16s16 6 16 16z"/><circle cx="11" cy="16" r="6"/><circle cx="45" cy="16" r="6"/><path d="M0 40c0-7 4-12 11-12 3 0 5 1 6 2-3 3-5 6-5 10zM56 40c0-7-4-12-11-12-3 0-5 1-6 2 3 3 5 6 5 10z"/></svg></div>
      <div class="feature-label">OUR TEAM</div>
    </div>
    <div class="feature" style="left:741px">
      <div class="feature-icon"><svg width="44" height="52" viewBox="0 0 44 52" fill="#fff"><circle cx="22" cy="20" r="16"/><path d="M12 32l-5 18 8-4 5 6 2-16zM32 32l5 18-8-4-5 6-2-16z"/></svg></div>
      <div class="feature-label">OUR QUALITY</div>
    </div>
    <div class="feature" style="left:924px">
      <div class="feature-icon"><svg width="46" height="46" viewBox="0 0 46 46" fill="#fff"><rect x="3" y="20" width="9" height="22" rx="2"/><path d="M16 22l9-16c4 0 6 3 5 7l-2 6h12c3 0 5 3 4 6l-4 14c-1 2-3 3-5 3H16z"/></svg></div>
      <div class="feature-label">TRUST</div>
    </div>
  </div>
  <span class="pointer"></span>
</section>

<section class="technology">
  <h3>TECHNOLOGY</h3>
  <p class="intro">Praesent interdum, neque eu efficitur vestibulum, neque felis laoreet sem, auctor blandit ipsum lectus a neque. Maecenas eleifend ipsum iaculis metus tincidunt iaculis.</p>
  <ul class="tech-list">
    <li style="left:277px;top:0"><svg width="12" height="12" viewBox="0 0 12 12"><path d="M1 6l3.5 4L11 2" fill="none" stroke="#fff" stroke-width="1.8"/></svg>Praesent interdum, neque eu efficitur vestibulum.</li>
    <li style="left:277px;top:42px"><svg width="12" height="12" viewBox="0 0 12 12"><path d="M1 6l3.5 4L11 2" fill="none" stroke="#fff" stroke-width="1.8"/></svg>laoreet sem, auctor blandit ipsum lectus a neque.</li>
    <li style="left:277px;top:84px"><svg width="12" height="12" viewBox="0 0 12 12"><path d="M1 6l3.5 4L11 2" fill="none" stroke="#fff" stroke-width="1.8"/></svg>Maecenas eleifend ipsum iaculis metus tincidunt iaculis.</li>
    <li style="left:651px;top:0"><svg width="12" height="12" viewBox="0 0 12 12"><path d="M1 6l3.5 4L11 2" fill="none" stroke="#fff" stroke-width="1.8"/></svg>Praesent interdum, neque eu efficitur vestibulum.</li>
    <li style="left:651px;top:42px"><svg width="12" height="12" viewBox="0 0 12 12"><path d="M1 6l3.5 4L11 2" fill="none" stroke="#fff" stroke-width="1.8"/></svg>laoreet sem, auctor blandit ipsum lectus a neque.</li>
    <li style="left:651px;top:84px"><svg width="12" height="12" viewBox="0 0 12 12"><path d="M1 6l3.5 4L11 2" fill="none" stroke="#fff" stroke-width="1.8"/></svg>Maecenas eleifend ipsum iaculis metus tincidunt iaculis.</li>
  </ul>
  <a class="btn-apps" href="#">GET OUR APPLICATIONS</a>
</section>

<section class="platforms">
  <h2 class="section-title">We use the following <strong>Platforms</strong></h2>
  <p class="lead">Sed semper est risus, a faucibus nibh vestibulum rhoncus. Ut ultrices ullamcorper dapibus. Aenean consequat in nisi eu vehicula. Vivamus et justo a arcu porttitor gravida eget id augue. Curabitur eu volutpat dui. In porta efficitur nunc, quis suscipit tellus congue nec.</p>
  <article class="platform-card" style="left:187px">
    <div class="card-icon"><span></span></div>
    <h4>Orbis Apps</h4>
    <div class="sub">Development Services</div>
    <p>Sed semper est risus, a faucibus nibh vestibulum rhoncus. Ut ultrices ullamcorper dapibus.</p>
    <a class="btn-outline" href="#">VIEW APPS</a>
  </article>
  <article class="platform-card" style="left:483px">
    <div class="card-icon"><span></span></div>
    <h4>Nimble Apps</h4>
    <div class="sub">Development Services</div>
    <p>Sed semper est risus, a faucibus nibh vestibulum rhoncus. Ut ultrices ullamcorper dapibus.</p>
    <a class="btn-outline" href="#">VIEW APPS</a>
  </article>
  <article class="platform-card" style="left:779px">
    <div class="card-icon"><span></span></div>
    <h4>Panea Apps</h4>
    <div class="sub">Development Services</div>
    <p>Sed semper est risus, a faucibus nibh vestibulum rhoncus. Ut ultrices ullamcorper dapibus.</p>
    <a class="btn-outline" href="#">VIEW APPS</a>
  </article>
</section>

<section class="showcase">
  <div class="showcase-banner" role="img" aria-label="Blurred photo of a crowd at a street festival"></div>
  <div class="showcase-devices" role="img" aria-label="Three smartphones showing the festival app screens"></div>
  <div class="showcase-copy">
    <h5>HARBOUR STREET FESTIVAL APP</h5>
    <div class="showcase-actions">
      <a class="square-btn" href="#"><span></span></a>
      <a class="square-btn" href="#"><span></span></a>
      <a class="details-btn" href="#">VIEW DETAILS</a>
    </div>
  </div>
  <div class="slider-dots" style="left:1015px;top:281px"><i></i><i class="on"></i><i></i></div>
</section>

<section class="clients" aria-label="Clients">
  <span class="client" style="left:21px;width:44px"></span>
  <span class="client" style="left:112px;width:44px;border-radius:50%"></span>
  <span class="client" style="left:200px;width:54px"></span>
  <span class="client" style="left:300px;width:50px"></span>
  <span class="client" style="left:410px;width:46px"></span>
  <span class="client" style="left:515px;width:60px"></span>
  <span class="client" style="left:628px;width:90px"></span>
  <span class="client" style="left:765px;width:103px"></span>
</section>

<footer class="site-footer">
  <div class="blog">
    <h6 class="footer-heading">LATEST BLOG UPDATES</h6>
    <div class="blog-item" style="margin-top:24px">Enhance Learning with a Course Evaluation System<time>September 19, 2014</time></div>
    <div class="blog-item" style="margin-top:20px">Brightpoll Sponsors the Fieldwork Data Society (FDS) Conference<time>September 19, 2014</time></div>
    <div class="blog-item" style="margin-top:20px">It's Never Too Early to Think About Course Evaluations<time>September 19, 2014</time></div>
    <div class="blog-item" style="margin-top:20px">New Worksheet: Personalizing Survey Email Invitations and Reminders<time>September 19, 2014</time></div>
  </div>
  <div class="newsletter">
    <h6 class="footer-heading">NEWSLETTER</h6>
    <div class="signup"><span class="field">Email Address</span><span class="submit">SUBMIT</span></div>
    <h6 class="footer-heading" style="margin-top:40px">CONNECT WITH US</h6>
    <ul class="connect">
      <li><i></i>Blog</li>
      <li><i></i>Chirpline</li>
      <li><i></i>Workgrid</li>
      <li><i></i>Friendhub</li>
    </ul>
  </div>
  <address class="contact-box">
    <h6 class="footer-heading">CONTACT US</h6>
    <p style="margin-top:14px"><strong>Velquin Solutions</strong></p>
    <p style="margin-top:4px">12 Arden Court<br>Fenwick Street, Islington<br>N1 4QT</p>
    <p style="margin-top:14px"><strong>UK 020 7946 0321</strong><br>sales@velquinsolutions.com</p>
    <p style="margin-top:14px"><strong>Worldwide +44 20 7946 0321</strong><br>info@velquinsolutions.com</p>
  </address>
</footer>

<div class="footer-bar">
  <p class="legal">Copyright © 2014 Velquin Solutions. All rights reserved.<br>Privacy Policy | Legal Statement | Software Legal and Service Agreements</p>
  <div class="brand-small"><span class="dot"></span><span class="name">Velquin Solutions</span></div>
</div>

</body>
</html>
```